Design a clean and bold corporate Presentation for Brand New Company

Task Outline
Create corporate presentation

Task Description
Creation of Powerpoint corporate presentation using the content below.

The presentation is 10 slides long.

PLEASE NOTE: THE FULL CONTENT AND STRUCTURE OF THE CORPORATE PRESENTATION ARE INCLUDED IN ATTACHMENT.

Corporate presentation
– structure is as attached in file titled “plumvo Corp Pres”.

We would like a clean, modern presentation with the use of graphics (not photos) to support key points. We need the graphics designed – NOT clip-art, as we aim to use these on the web-site (examples of preferred design below).

plumvo is a new start-up company where we aim to combine the best of recruitment and IT service delivery expertise to:

Offer access to the best possible resources in the UK and Globally, in a range of commercial models that offer cost savings and agility. Using best practice service delivery to assure quality.

Our foundations are outstanding employee satisfaction, and fantastic customer service.

Do’s
- Be bold ! Use clean design graphics to better highlight and explain products and capabilities in the corporate presentation
- Professional, contemporary and clean – our target market are new IT businesses that are web-savvy.
- Use single colour graphics
- Use a consistent theme through-out
- Establish a design that would translate easily to the web
- Establish a design that would translate into a Powerpoint template
- Use Calibri font

Don’ts
- Use generic photos e.g. “smiling IT professional” ;-)
- No cartoon graphics
- Use complex multi-colour graphics
- Use standard Powerpoint clip-art
- Create a large file
- Use animation / transitions

Output
Powerpoint file – 2011 but compatible with 2007

Deadline
+ 1 week from issue.

What is your industry?
IT Recruitment, Consulting, Professional Services

Target Market
• New customers - Our target market are high growth companies with a heavy reliance on IT, 50-250 employees, based in UK.
• Hiring candidates – IT professionals who are potential hiring candidates for our customers.
• Employees – typically graduates who will be looking for their first/second professional role

What design styles do you like that you would like to reflect in the design?
• http://www.qrtl.com/what-we-offer/
• http://www.zenthic.io/platform-as-a-service/zenthic-sky-harbor
• www.lumo.com

Do you have any other info or links you want to share?
- Corporate presentation
- Logo image

Target Market(s)

Target Market

Industry/Entity Type

It Company

Font styles to use
Sans Serif

Colors
34a6d7
faa54b
d2a4cc
85acd3

Requirements
Must have
• Do’s
• - Be bold ! Use clean design graphics to better highlight and explain products and capabilities in the corporate presentation
• - Professional, contemporary and clean – our target market are new IT businesses that are web-savvy.
• - Use single colour graphics
• - Use a consistent theme through-out
• - Establish a design that would translate easily to the web
• - Establish a design that would translate into a Powerpoint template
• - Use Calibri font
Nice to have
• Use of transparent background imagery
Should not have
• Don’ts
• - Use generic photos e.g. “smiling IT professional” ;-)
• - No cartoon graphics
• - Use complex multi-colour graphics
• - Use standard Powerpoint clip-art
• - Create a large file
• - Use animation / transitions

```html
<!DOCTYPE html>
<html lang="en">
<head>
<meta charset="utf-8">
<title>plumvo Corp Pres</title>
<link rel="stylesheet" href="https://fonts.googleapis.com/css2?family=Quicksand:wght@400;500;700&display=swap">
<style>
  :root {
    --backdrop: #000000;
    --brand-blue: #34a6d7;
    --brand-orange: #faa54b;
    --deep-blue: #2a4fa0;
    --white: #ffffff;
    --night: #1a2430;
  }
  * { box-sizing: border-box; margin: 0; padding: 0; }
  html, body { width: 1060px; height: 1200px; overflow: hidden; background: var(--backdrop); }
  body { position: relative; font-family: "Quicksand", sans-serif; color: var(--white); }

  .slide { position: absolute; left: 23px; width: 1018px; height: 573px; overflow: hidden; }
  .slide--resourcing { top: 19px; }
  .slide--iteration { top: 609px; }

  .page-number {
    position: absolute; left: 955px; top: 30px; width: 32px; height: 32px; border-radius: 50%;
    background: var(--brand-blue); color: var(--white); font-size: 14px; font-weight: 500;
    display: flex; align-items: center; justify-content: center;
  }

  /* Slide 4 */
  .intro-panel { position: absolute; left: 0; top: 0; width: 585px; height: 573px; background: var(--brand-blue); }
  .bracket-title { position: absolute; font-weight: 400; }
  .bracket-title svg { position: absolute; left: 0; top: 0; overflow: visible; }
  .intro-panel .bracket-title { left: 61px; top: 42px; width: 223px; height: 59px; }
  .intro-panel .bracket-title span { position: absolute; left: 17px; top: 8px; font-size: 32px; }
  .intro-subtitle { position: absolute; left: 61px; top: 118px; font-size: 23px; }
  .value-list { list-style: none; }
  .value-item { position: absolute; left: 61px; display: flex; align-items: center; font-size: 21px; }
  .value-item svg { width: 26px; height: 26px; margin-right: 35px; }
  .value-item:nth-child(1) { top: 226px; }
  .value-item:nth-child(2) { top: 337px; }
  .value-item:nth-child(3) { top: 448px; }

  .dice-photo {
    position: absolute; left: 585px; top: 0; width: 433px; height: 573px;
    background: radial-gradient(circle at 55% 30%, #e0a23a 0%, #b98652 25%, #8a6a50 55%, #4a3a30 100%);
  }
  .photo-wordmark {
    position: absolute; left: 20px; top: 505px; font-size: 36px; font-weight: 700; color: var(--brand-orange);
  }

  /* Slide 5 */
  .slide--iteration { background: linear-gradient(180deg, #24303c 0%, var(--night) 45%, #10161d 100%); }
  .skyline-photo { position: absolute; inset: 0;
    background: linear-gradient(100deg, rgba(40,60,80,0.6) 0%, rgba(20,30,40,0.2) 40%, rgba(60,70,80,0.35) 70%, rgba(15,20,28,0.6) 100%); }
  .slide--iteration .bracket-title { left: 265px; top: 16px; width: 473px; height: 51px; }
  .slide--iteration .bracket-title span { position: absolute; left: 12px; top: 10px; font-size: 25px; }
  .diagram { position: absolute; left: 0; top: 0; }
  .pillar-label { position: absolute; text-align: center; font-size: 25px; line-height: 1.25; transform: translate(-50%, -50%); }
  .pillar-label--time { left: 480px; top: 145px; }
  .pillar-label--cost { left: 189px; top: 419px; }
  .pillar-label--quality { left: 777px; top: 408px; }
  .pillar-text { position: absolute; font-size: 19px; line-height: 1.3; white-space: nowrap; }
  .pillar-text--time { left: 562px; top: 120px; }
  .pillar-text--cost { left: 242px; top: 496px; transform: translateX(-50%); text-align: center; }
  .pillar-text--quality { left: 768px; top: 478px; transform: translateX(-50%); text-align: center; }
  .center-wordmark {
    position: absolute; left: 476px; top: 326px; transform: translate(-50%, -50%);
    font-size: 62px; font-weight: 700; color: var(--deep-blue); line-height: 1;
  }
</style>
</head>
<body>

<section class="slide slide--resourcing">
  <div class="intro-panel">
    <h1 class="bracket-title">
      <svg width="223" height="59" fill="none" stroke="#fff" stroke-width="1.5">
        <path d="M0 14V0H14M209 0H223V14M223 45V59H209M14 59H0V45"/>
      </svg>
      <span>Resourcing</span>
    </h1>
    <p class="intro-subtitle">We wanted to do something different</p>
    <ul class="value-list">
      <li class="value-item"><svg viewBox="0 0 26 26"><circle cx="13" cy="13" r="12" fill="#fff"/><path d="M6 19L20 7" stroke="#34a6d7" stroke-width="3"/></svg>Always deliver.</li>
      <li class="value-item"><svg viewBox="0 0 26 26"><circle cx="13" cy="13" r="12" fill="#fff"/><path d="M6 19L20 7" stroke="#34a6d7" stroke-width="3"/></svg>Charge less, for doing more.</li>
      <li class="value-item"><svg viewBox="0 0 26 26"><circle cx="13" cy="13" r="12" fill="#fff"/><path d="M6 19L20 7" stroke="#34a6d7" stroke-width="3"/></svg>Bring some rigour.</li>
    </ul>
  </div>
  <div class="dice-photo" role="img" aria-label="Photo of red and blue dice tumbling into a glass">
    <span class="photo-wordmark">plumvo</span>
  </div>
  <span class="page-number">4</span>
</section>

<section class="slide slide--iteration">
  <div class="skyline-photo" role="img" aria-label="Photo looking up at glass office towers against a dusky sky"></div>
  <h2 class="bracket-title">
    <svg width="473" height="51" fill="none" stroke="#fff" stroke-width="1.5">
      <path d="M0 12V0H12M461 0H473V12M473 39V51H461M12 51H0V39"/>
    </svg>
    <span>An iteration of traditional resourcing</span>
  </h2>
  <svg class="diagram" width="1018" height="573" viewBox="0 0 1018 573" fill="none">
    <path d="M420 160A64 64 0 0 1 544 145" stroke="#34a6d7" stroke-width="2"/>
    <path d="M125 455A74 74 0 0 1 250 375" stroke="#2a4fa0" stroke-width="2"/>
    <path d="M705 440A80 80 0 0 1 850 375" stroke="#faa54b" stroke-width="2"/>
    <g fill="#34a6d7">
      <path transform="translate(480 287) rotate(-90)" d="M0 -6H38V-15L59 0L38 15V6H0Z"/>
      <path transform="translate(356 343) rotate(149)" d="M0 -6H42V-15L63 0L42 15V6H0Z"/>
      <path transform="translate(594 332) rotate(29)" d="M0 -6H45V-15L66 0L45 15V6H0Z"/>
    </g>
  </svg>
  <div class="center-wordmark">plumvo</div>
  <div class="pillar-label pillar-label--time">TIME<br>to hire</div>
  <p class="pillar-text pillar-text--time">Local and global resourcing<br>combined to deliver hard to find<br>resources fast.</p>
  <div class="pillar-label pillar-label--cost">COST<br>to hire</div>
  <p class="pillar-text pillar-text--cost">Share the financial benefits of<br>resourcing more efficiently together.</p>
  <div class="pillar-label pillar-label--quality">QUALITY<br>of hires</div>
  <p class="pillar-text pillar-text--quality">Bring IT service delivery quality to<br>the resourcing market to improve<br>process and quality of hires.</p>
  <span class="page-number">5</span>
</section>

</body>
</html>
```